Website design for an Online pastry shop

Website Name : www.lanternandplum.example

Description of the website and its target audience
We are a premium pastry company producing delicious cakes, macarons, cookies, gelato, and other sweet dessert. Our differentiation is that our products are freshly produced with premium quality imported ingredients and one bite into our products set us apart from other bakery shop. We online retail online so as to provide high quality products at a affordable cost. Our products has received raving reviews by many food enthusiast even the hard to please ones. The products contain more natural ingredients and we do not add preservatives. The return rates for our pastry is almost 80%. You only need to try once to be return customers. Our greatest challenge is getting customer to take the first bite. We are so sure of our products that we are going to give people free food tasting.

We are based in China but all our products are developed by award winning chefs from 5 stars hotel. The target customer is woman 16 to 40+ in china. Working class ladies and demand high quality products. A modern, sophisticated and minimalist website

This is a competitive market and image is crucial for such a food ‘conscious ’ orientated customer. They want to feel that they are buying from a reliable company that take great effort to ensure food cleaniness and safety yet affordable price. We make almost 98% of sub ingredients ourselves and we make it by hand.

Style/theme ideas for the web page design
I am looking for a elegant a little rustic, handmade feel yet sophisticated design - one that is easy to the eye yet functional and easy for the user to navigate through. Good play of fonts to give let it feel unique and customised. Black and white is our corporate colours. However, we do not want black background as it does not tease the taste bud. All our colours should come from our products. Customers should be very close to our products. They eat with their eyes first. Black and white is just accent.

Inspirational and competitors websites
http://www.47tart.example/ ( Key competitor )
I like the simple, clean look. The products are the key focus
https://www.pelvora.example/
clean, fresh and different. Attractive with purpose. Feminine
http://moatandwillow.example/
this has a great layout - lots of information and nicely presented. Very sweet and feminine
http://www.storeharbourly.example/
product features is the focus
http://www.janetobrill.example/store/
fun, feminine, rustic

Number of pages needed : 6 ( Uncoded PSD design only )
Page descriptions
Home Page - This page will show what makes our products stand out from the competitors and provide an introduction of who we are.
2nd page : Product catalogue
3nd page: Detail Product page with pictures and descriptions. Select products size and add to cart....
4rd page: Brand Story with pictures and descriptions.
5th page Contact Us : Here they can contact or schedule an appointment for free product tasting
6th page : Check out page

• Please see the project wire frame file " main page.png " or file number 70

```html
<!DOCTYPE html>
<html lang="en">
<head>
<meta charset="utf-8">
<title>Lantern &amp; Plum — Artisan Pastry</title>
<link rel="stylesheet" href="https://fonts.googleapis.com/css2?family=Noto+Serif:wght@400;700&family=Cormorant+SC:wght@500;600&display=swap">
<style>
:root{
  --pink:#e6649a;
  --pink-deep:#d0457f;
  --pink-line:#eb8db4;
  --ink:#333333;
  --topbar:#f4f4f4;
  --tagline-bg:#f6f6f6;
  --footer:#3f3f3f;
  --footer-bottom:#333333;
  --footer-text:#f1f1f1;
  --bullet:#8a8a8a;
  --white:#ffffff;
}
*{box-sizing:border-box;margin:0;padding:0}
html,body{width:899px;height:1200px;overflow:hidden;background:var(--white)}
body{position:relative;font-family:"Noto Serif",Georgia,serif;color:var(--ink)}
.sc{font-family:"Cormorant SC","Noto Serif",serif;font-weight:600}
a{color:inherit;text-decoration:none}

.topbar{position:absolute;left:0;top:0;width:899px;height:32px;background:var(--topbar)}
.topbar .promo{position:absolute;left:79px;top:7px;font-size:14px}
.topbar .promo b{color:var(--pink);font-weight:600}
.account{position:absolute;right:93px;top:0;height:32px;display:flex}
.account a{display:flex;align-items:center;gap:3px;padding:0 5px;font-size:13.5px;border-left:1px solid #e2e2e2}
.account a:first-child{border-left:0}

.brand{position:absolute;left:0;top:82px;width:899px;text-align:center}
.brand .mark{display:inline-flex;align-items:center;gap:10px;font-size:19px;color:var(--pink);letter-spacing:.5px}
.brand .dot{width:30px;height:30px;border-radius:50%;background:var(--pink)}
.mainnav{position:absolute;left:0;top:135px;width:899px;display:flex;justify-content:center;align-items:center;gap:12px;font-size:15.5px}
.mainnav a.current{color:var(--pink)}
.mainnav .sep{width:5px;height:5px;border-radius:50%;background:#9a9a9a}

.hero{position:absolute;left:0;top:178px;width:899px;height:255px;border-top:2px solid var(--pink-line);border-bottom:2px solid var(--pink-line);
  background:
    radial-gradient(ellipse 45% 60% at 38% 35%,rgba(60,30,20,.95),transparent 70%),
    radial-gradient(ellipse 40% 18% at 38% 72%,rgba(238,224,200,.9),transparent 75%),
    radial-gradient(ellipse 40% 60% at 85% 40%,rgba(176,130,92,.9),transparent 75%),
    linear-gradient(90deg,#5e3a28,#7a5238 55%,#9c7352)}

.tagline{position:absolute;left:0;top:437px;width:899px;height:89px;background:var(--tagline-bg)}
.tagline p{position:absolute;left:128px;width:630px;top:33px;text-align:center;font-size:14.4px;line-height:18px;color:#3d3d3d}
.tagline .tick{position:absolute;left:437px;width:12px;height:6px;background:var(--pink);opacity:.55;border-radius:2px}

.featured h2{position:absolute;left:0;top:538px;width:880px;text-align:center;font-weight:400;font-size:24px;color:var(--pink)}
.featured .rule{position:absolute;left:368px;top:576px;width:150px;height:1px;background:#e8e8e8}
.featured .rule::after{content:"";position:absolute;left:70px;top:-3px;width:6px;height:6px;border-radius:50%;background:#d7b99a}
.card{position:absolute;top:600px;width:180px;height:153px;border-top:2px dashed #f0a6c4;border-bottom:2px dashed #f0a6c4}
.card .label{position:absolute;left:33px;top:66px;width:114px;height:30px;background:rgba(255,255,255,.72);
  text-align:center;font-size:23px;line-height:30px;color:#4a4a4a}
.card .label.pink{color:var(--pink)}

.mailing{position:absolute;left:0;top:773px;width:899px;height:131px;
  background:radial-gradient(ellipse at 20% 40%,#c45a85,transparent 60%),linear-gradient(90deg,#d46f98,#e190b2 60%,#da7ea4)}
.mailing h3{position:absolute;left:0;top:12px;width:899px;text-align:center;font-weight:400;font-size:19px;color:var(--white)}
.mailing form{position:absolute;left:255px;top:47px;width:388px;height:34px;display:flex;border:1px solid rgba(255,255,255,.85)}
.mailing .email{flex:1;padding-left:11px;font-size:12px;color:var(--white);line-height:32px}
.mailing .submit{width:80px;background:var(--pink-deep);color:var(--white);font-weight:700;font-size:13px;text-align:center;line-height:32px}
.social{position:absolute;left:324px;top:87px;display:flex;gap:6px}
.social span{width:25px;height:25px;border-radius:50%;background:var(--pink-deep);box-shadow:0 0 0 2px rgba(255,255,255,.35)}

.footer{position:absolute;left:0;top:904px;width:899px;height:258px;background:var(--footer);color:var(--footer-text)}
.col{position:absolute}
.col h4{font-weight:400;font-size:14px;margin-bottom:4px}
.col li{list-style:none;font-size:10.5px;line-height:18px;padding-left:9px;position:relative}
.col li::before{content:"";position:absolute;left:0;top:7px;width:5px;height:5px;background:var(--bullet)}
.col p{font-size:10.3px;line-height:13.5px;width:200px}
.contact{position:absolute;top:207px;display:flex;align-items:flex-start;gap:5px;font-size:10.5px;line-height:13.5px}
.footer .brand-foot{position:absolute;left:600px;top:54px;width:218px;font-size:16px;color:var(--pink);display:flex;justify-content:center;align-items:center;gap:8px}
.footer .brand-foot .dot{width:24px;height:24px;border-radius:50%;background:var(--pink)}
.footer .photo{position:absolute;left:600px;top:105px;width:218px;height:133px;
  background:radial-gradient(ellipse 55% 30% at 45% 40%,rgba(80,30,60,.9),transparent 75%),
    radial-gradient(ellipse 55% 25% at 45% 68%,rgba(238,214,150,.95),transparent 75%),#ffffff}
.copyright{position:absolute;left:0;top:1162px;width:899px;height:38px;background:var(--footer-bottom);color:var(--footer-text);text-align:center;font-size:11px;line-height:38px}
</style>
</head>
<body>
<header>
  <div class="topbar">
    <span class="promo sc">Free Delivery For Order&nbsp; Above <b>$50</b></span>
    <nav class="account sc">
      <a href="#"><svg width="11" height="10" viewBox="0 0 11 10"><rect x="0.5" y="1.5" width="10" height="8" rx="1" fill="#e6649a"/><circle cx="5.5" cy="5" r="1.8" fill="#fff"/></svg>Login</a>
      <a href="#"><svg width="10" height="11" viewBox="0 0 10 11"><circle cx="5" cy="3" r="2.6" fill="#e6649a"/><path d="M0.5 11c0-3 2-4.5 4.5-4.5s4.5 1.5 4.5 4.5z" fill="#e6649a"/></svg>Sign up</a>
      <a href="#"><svg width="13" height="11" viewBox="0 0 13 11"><path d="M0 1h2l2 6h7l1.5-4.5H3" fill="none" stroke="#e6649a" stroke-width="1.4"/><circle cx="5" cy="9.5" r="1" fill="#e6649a"/><circle cx="10" cy="9.5" r="1" fill="#e6649a"/></svg>Cart</a>
    </nav>
  </div>
  <div class="brand"><span class="mark"><span class="dot"></span>LANTERN &amp; PLUM</span></div>
  <nav class="mainnav sc">
    <a href="#">Cakes</a><span class="sep"></span>
    <a href="#" class="current">Macarons</a><span class="sep"></span>
    <a href="#">Cookies</a><span class="sep"></span>
    <a href="#">Gelato</a><span class="sep"></span>
    <a href="#">Tasting Room</a><span class="sep"></span>
    <a href="#">About Us</a>
  </nav>
</header>

<main>
  <div class="hero" role="img" aria-label="Close-up of a layered chocolate cake slice topped with chocolate shavings on a wooden board"></div>

  <section class="tagline">
    <span class="tick" style="top:12px"></span>
    <p>We value flavor over fuss.Artisan handcrated and other gourment confection deliverded direct your dour</p>
    <span class="tick" style="top:83px"></span>
  </section>

  <section class="featured">
    <h2>Featured</h2>
    <div class="rule"></div>
    <div class="card" style="left:80px;background:radial-gradient(ellipse at 50% 70%,#f3ece4,transparent 70%),linear-gradient(160deg,#e6cfb4,#d8b48c 70%,#b07a4c)" role="img" aria-label="Soft-focus cake on a plate"><span class="label pink sc">Cakes</span></div>
    <div class="card" style="left:268px;background:radial-gradient(ellipse at 55% 65%,#e9d8c6,transparent 60%),linear-gradient(180deg,#8a7058,#c48a50)" role="img" aria-label="Stacked macarons beside a cup of tea"><span class="label sc">Macrons</span></div>
    <div class="card" style="left:455px;background:radial-gradient(ellipse 70% 45% at 50% 30%,#a52634,transparent 80%),linear-gradient(180deg,#f3ece8,#f0dcb0 70%,#c08850)" role="img" aria-label="Cherry-topped cheesecake"><span class="label sc">Cookies</span></div>
    <div class="card" style="left:643px;background:radial-gradient(ellipse 60% 50% at 50% 55%,#e4d6c4,transparent 80%),#ece6f0" role="img" aria-label="Round cream gelato cake with white petal decoration"><span class="label sc">Gelato</span></div>
  </section>

  <section class="mailing">
    <h3>Join our Mailing List</h3>
    <form><span class="email">Email Address</span><span class="submit">SUBMIT</span></form>
    <div class="social" aria-label="Social links"><span></span><span></span><span></span><span></span><span></span><span></span><span></span></div>
  </section>
</main>

<footer class="footer">
  <div class="col" style="left:85px;top:18px"><h4>CAKES</h4><ul><li>Contrary to popular</li><li>Contrary to popular</li><li>Contrary to popular</li></ul></div>
  <div class="col" style="left:234px;top:18px"><h4>COOKIES</h4><ul><li>Contrary to popular</li><li>Contrary to popular</li><li>Contrary to popular</li></ul></div>
  <div class="col" style="left:385px;top:18px"><h4>ABOUT</h4><p>There are many variations of passag-<br>es of Lorem Ipsum available, but the majority have suffered alteration in some form,</p></div>
  <div class="col" style="left:85px;top:106px"><h4>MACACRONS</h4><ul><li>Contrary to popular</li><li>Contrary to popular</li><li>Contrary to popular</li></ul></div>
  <div class="col" style="left:234px;top:106px"><h4>GELATO</h4><ul><li>Contrary to popular</li><li>Contrary to popular</li><li>Contrary to popular</li></ul></div>
  <div class="col" style="left:387px;top:106px"><h4>CUSTOMER SERVICES</h4><ul><li>Contrary to popular</li><li>Contrary to popular</li><li>Contrary to popular</li></ul></div>

  <div class="contact" style="left:86px"><svg width="12" height="12" viewBox="0 0 12 12"><path d="M2 0.5l2 2.5-1 1.5c.8 1.6 2 2.8 3.5 3.5l1.5-1 2.5 2-1 2.5C4.5 11.5 0.5 7.5 0 2z" fill="#e6649a"/></svg>Call Now:800-555-0142</div>
  <div class="contact" style="left:226px"><svg width="13" height="10" viewBox="0 0 13 10"><rect x="0.5" y="0.5" width="12" height="9" fill="#e6649a"/><path d="M0.5 0.5l6 5 6-5" fill="none" stroke="#3f3f3f" stroke-width="1"/></svg>Email:800-555-0142</div>
  <div class="contact" style="left:358px"><svg width="10" height="13" viewBox="0 0 10 13"><path d="M5 13C1.5 8 0 6.5 0 4.5a5 5 0 0110 0C10 6.5 8.5 8 5 13z" fill="#e6649a"/><circle cx="5" cy="4.6" r="1.8" fill="#3f3f3f"/></svg><span>Address: Marrowgate Lane 42b<br>10117 Larkfield Germany</span></div>

  <div class="brand-foot"><span class="dot"></span>LANTERN &amp; PLUM</div>
  <div class="photo" role="img" aria-label="Blueberry cheesecake with a slice cut out"></div>
</footer>
<div class="copyright">All Rights Reserved @ Lantern &amp; Plum 2015</div>
</body>
</html>
```